Wedding Program

Miriam and Owen are getting married. They are looking for a simple 4-page program that conveys the special day. Venue is a museum in a large East-Coast city: classic 18th century, formal. Ceremony is non-religious. Party includes a photo booth and DJ.

He's a math geek - she's an activist/educator.

Please incorporate unique design sensibility - be creative! Colors of purple, eggplant, ivory, and gray are the couple's choice. Fall motif OK.

Target Market(s)

ages 25 - 85, members of a family

Industry/Entity Type

Graphic Design

Font styles to use
Serif
Decorative

Colors
8769ae
b7a5cd
fece3e
f78f20
757575
cfcfcf
6b449b
a64599
fffaee

Requirements
Must have
• Readable, attractive 4-color design using the copy and image provided in the attachment.
Nice to have
• It's a LOVE-ly day for a wedding - be creative!
Should not have
• Avoid flowery girly-girl fonts or obvious hearts and flowers stuff.

```html
<!DOCTYPE html>
<html lang="en">
<head>
<meta charset="utf-8">
<title>Miriam &amp; Owen — Wedding Program</title>
<link rel="stylesheet" href="https://fonts.googleapis.com/css2?family=Great+Vibes&family=Cinzel:wght@400;600&family=Montserrat:wght@700&display=swap">
<style>
  :root {
    --purple: #6b449b;
    --lilac: #b7a5cd;
    --lavender: #8769ae;
    --ivory: #fffaee;
    --paper: #ffffff;
    --gray: #757575;
    --light-gray: #cfcfcf;
    --backdrop: #e8e6ea;
  }
  * { box-sizing: border-box; margin: 0; padding: 0; }
  html, body { width: 1200px; height: 1200px; overflow: hidden; }
  body {
    background: var(--backdrop);
    font-family: "Cinzel", serif;
    color: var(--gray);
  }
  .program {
    position: absolute; left: 149px; top: 15px;
    display: grid;
    grid-template-columns: 431px 431px;
    grid-template-rows: 575px 575px;
    gap: 20px 40px;
  }
  .page {
    position: relative; overflow: hidden;
    background: var(--paper);
    box-shadow: 0 2px 10px rgba(0,0,0,.12);
  }
  .band { position: absolute; left: 0; top: 0; width: 431px; height: 112px; display: block; }
  .band-tagline {
    position: absolute; top: 26px; width: 100%; text-align: center;
    color: var(--paper); font-size: 13px; letter-spacing: 2px;
  }
  .pattern {
    position: absolute; left: 0; bottom: 0; width: 300px; height: 360px;
    background: radial-gradient(ellipse at 30% 60%, rgba(183,165,205,.28), rgba(183,165,205,0) 70%);
  }
  .monogram {
    position: absolute; right: 26px; bottom: 22px; width: 62px; height: 44px;
    border-radius: 22px;
    background: linear-gradient(90deg, rgba(183,165,205,.45), rgba(135,105,174,.35));
  }

  /* cover */
  .cover-names {
    position: absolute; top: 140px; width: 100%; text-align: center;
    font-family: "Great Vibes", cursive; font-weight: 400; color: var(--purple); line-height: .9;
  }
  .cover-names .name { display: block; font-size: 96px; }
  .cover-names .and { display: block; font-size: 30px; margin: -6px 0 -4px; }
  .cover-details { position: absolute; top: 392px; width: 100%; text-align: center; }
  .cover-details .intro { font-size: 12px; letter-spacing: 1.5px; }
  .cover-details .couple {
    font-family: "Montserrat", sans-serif; font-weight: 700; color: var(--purple);
    font-size: 15px; letter-spacing: 1px; margin: 6px 0 12px;
  }
  .cover-details .when { font-size: 12px; line-height: 1.55; letter-spacing: 1px; }

  /* interior */
  .page-title { position: absolute; left: 40px; top: 108px; width: 360px; height: 64px; }
  .page-title svg { position: absolute; left: 0; top: 0; }
  .page-title h2 {
    position: absolute; left: 40px; top: 10px;
    font-family: "Great Vibes", cursive; font-weight: 400;
    color: var(--purple); font-size: 38px; white-space: nowrap;
  }
  .content { position: absolute; top: 190px; left: 40px; right: 40px; text-align: center; }

  .letter p { font-size: 11.5px; line-height: 1.6; letter-spacing: .5px; margin-bottom: 12px; }

  .party dt { color: var(--purple); font-weight: 600; font-size: 12px; letter-spacing: 1px; }
  .party dd { font-size: 11px; margin-bottom: 12px; letter-spacing: .5px; white-space: nowrap; }

  .order li { list-style: none; font-size: 11.5px; letter-spacing: .8px; margin-bottom: 14px; }
</style>
</head>
<body>
<main class="program">

  <!-- Cover -->
  <section class="page cover">
    <svg class="band" viewBox="0 0 431 112" aria-hidden="true">
      <path fill="var(--purple)" d="M0 0 H431 V78 C412 112 344 112 323 78 C302 112 236 112 215 78 C194 112 129 112 108 78 C87 112 21 112 0 78 Z"/>
    </svg>
    <p class="band-tagline">IT'S A LOVE-LY DAY FOR A WEDDING</p>
    <h1 class="cover-names">
      <span class="name">Miriam</span>
      <span class="and">and</span>
      <span class="name">Owen</span>
    </h1>
    <div class="cover-details">
      <p class="intro">THE MARRIAGE CELEBRATION OF</p>
      <p class="couple">MIRIAM ASHFORD &amp; OWEN DELVAUX</p>
      <p class="when">SATURDAY, OCTOBER 15, 2016<br>AT 4 PM IN THE AFTERNOON<br>HARTWELL HALL<br>RIVERTON, MARYLAND</p>
    </div>
  </section>

  <!-- Welcome -->
  <section class="page welcome">
    <svg class="band" viewBox="0 0 431 112" aria-hidden="true">
      <path fill="var(--purple)" d="M0 0 H431 V60 C412 96 344 96 323 64 C302 96 236 96 215 64 C194 96 129 96 108 64 C87 96 21 96 0 60 Z"/>
    </svg>
    <div class="pattern" role="img" aria-label="Faint line-drawn floral pattern"></div>
    <div class="page-title">
      <svg width="360" height="64" viewBox="0 0 360 64" aria-hidden="true">
        <path d="M2 38 L10 32 L20 58 L34 6 H355" fill="none" stroke="var(--purple)" stroke-width="2"/>
      </svg>
      <h2>To our wedding guests</h2>
    </div>
    <div class="content letter">
      <p>Your presence here today adds greatly to our joy and happiness on this special day.</p>
      <p>Every marriage is the beginning of our lives together. We stand before you here, declaring our love, for each other we promise to be joined in marriage.</p>
      <p>We share with you our love, forever and always.</p>
      <p>We hope that you will continue to share in our new life, and we are grateful you have come with love and support.</p>
    </div>
    <div class="monogram" role="img" aria-label="Couple's ring monogram"></div>
  </section>

  <!-- Wedding party -->
  <section class="page party-page">
    <svg class="band" viewBox="0 0 431 112" aria-hidden="true">
      <path fill="var(--purple)" d="M0 0 H431 V60 C412 96 344 96 323 64 C302 96 236 96 215 64 C194 96 129 96 108 64 C87 96 21 96 0 60 Z"/>
    </svg>
    <div class="pattern" role="img" aria-label="Faint line-drawn floral pattern"></div>
    <div class="page-title">
      <svg width="360" height="64" viewBox="0 0 360 64" aria-hidden="true">
        <path d="M2 38 L10 32 L20 58 L34 6 H300" fill="none" stroke="var(--purple)" stroke-width="2"/>
      </svg>
      <h2>The Wedding Party</h2>
    </div>
    <dl class="content party">
      <dt>BRIDE AND GROOM</dt><dd>MIRIAM ASHFORD AND OWEN DELVAUX</dd>
      <dt>BRIDE'S PARENTS</dt><dd>HAROLD AND JOAN ASHFORD</dd>
      <dt>GROOM'S PARENTS</dt><dd>MARTIN AND CELIA DELVAUX</dd>
      <dt>BRIDESMAIDS</dt><dd>NINA BRANDT, TESSA HOLM, CLARA VOSS</dd>
      <dt>GROOMSMEN</dt><dd>FELIX MARSH, DEAN ORTO, PAUL KERR, IVAN LISLE</dd>
      <dt>GRANDPARENTS OF THE BRIDE</dt><dd>EDITH ASHFORD</dd>
      <dt>GRANDPARENTS OF THE GROOM</dt><dd>WALTER AND JUNE DELVAUX</dd>
      <dt>CELEBRANT</dt><dd>LENA MORAY</dd>
    </dl>
    <div class="monogram" role="img" aria-label="Couple's ring monogram"></div>
  </section>

  <!-- Processional -->
  <section class="page order-page">
    <svg class="band" viewBox="0 0 431 112" aria-hidden="true">
      <path fill="var(--purple)" d="M0 0 H431 V60 C412 96 344 96 323 64 C302 96 236 96 215 64 C194 96 129 96 108 64 C87 96 21 96 0 60 Z"/>
    </svg>
    <div class="pattern" role="img" aria-label="Faint line-drawn floral pattern"></div>
    <div class="page-title">
      <svg width="360" height="64" viewBox="0 0 360 64" aria-hidden="true">
        <path d="M2 38 L10 32 L20 58 L34 6 H230" fill="none" stroke="var(--purple)" stroke-width="2"/>
      </svg>
      <h2>Processional</h2>
    </div>
    <ol class="content order">
      <li>GREETING</li>
      <li>SEATING OF THE BRIDE</li>
      <li>PROCESSION OF THE BRIDE AND GROOM</li>
      <li>READING BY NORA ELLIS, FROM A LONG WALK</li>
      <li>EXCHANGE OF WEDDING RINGS</li>
      <li>EXCHANGE OF LOVE LETTERS</li>
      <li>WINE BOX AND LOVE LETTERS</li>
      <li>SIGNING OF MARRIAGE CERTIFICATE</li>
      <li>DECLARATION OF SUPPORT</li>
      <li>READING BY RUTH AVERY, THE OPEN DOOR</li>
      <li>DECLARATION OF MARRIAGE AND THE KISS</li>
      <li>RECESSIONAL</li>
    </ol>
    <div class="monogram" role="img" aria-label="Couple's ring monogram"></div>
  </section>

</main>
</body>
</html>
```